upmarket hotel in the mountains needs classy looking menu template

The Heathmere Lodge based in Bright needs two menu templates created ,

restaurant menu... layout is A3 folded in half that will have text on all 4 pa...

Industry/Entity Type

Hospitality

Requirements
Must have
• A combination of any of the logos provided, social media plugs

```html
<!DOCTYPE html>
<html lang="en">
<head>
<meta charset="utf-8">
<title>The Heathmere Lodge – Menu Spread</title>
<link rel="stylesheet" href="https://fonts.googleapis.com/css2?family=Cinzel:wght@400;700&family=Rye&family=Alfa+Slab+One&family=Montserrat:wght@500;700&family=Marcellus+SC&display=swap">
<style>
  :root {
    --backdrop: #2a2c32;
    --page-top: #45484d;
    --page-bottom: #2f3135;
    --gold: #f0ae1f;
    --gold-deep: #d9961a;
    --ink: #2c2c2c;
    --chalk: #e9e9e6;
    --chalk-soft: #bdbdb8;
  }
  * { margin: 0; padding: 0; box-sizing: border-box; }
  html, body { width: 1200px; height: 919px; overflow: hidden; background: var(--backdrop); }
  body { font-family: "Montserrat", sans-serif; color: var(--chalk); }

  .spread { position: absolute; left: 60px; top: 80px; width: 1080px; height: 760px; display: flex; box-shadow: 0 20px 50px rgba(0,0,0,.5); }
  .page { position: relative; width: 540px; height: 760px; background: linear-gradient(160deg, var(--page-top), var(--page-bottom)); overflow: hidden; }
  .page--left { box-shadow: inset -18px 0 30px -20px rgba(0,0,0,.6); }
  .page--right { box-shadow: inset 18px 0 30px -20px rgba(0,0,0,.6); }

  .brand { position: absolute; text-align: center; color: var(--gold); font-family: "Cinzel", serif; }
  .brand__mark { width: 22px; height: 22px; border: 1.5px solid var(--gold); margin: 0 auto 4px; }
  .brand__name { font-size: 17px; letter-spacing: 3px; line-height: 1.1; }
  .brand__sub { font-size: 8px; letter-spacing: 3px; }

  .art { position: absolute; }
  .art--rope { left: 0; top: 150px; width: 70px; height: 170px; background: linear-gradient(180deg, rgba(240,174,31,.55), rgba(240,174,31,.2)); border-radius: 0 40px 40px 0; }
  .art--food { left: 290px; top: 452px; width: 220px; height: 130px; background: radial-gradient(ellipse, #8d8d8a, #4a4c50 70%); border-radius: 50%; opacity: .8; }
  .art--kids { left: 30px; top: 140px; width: 130px; height: 120px; background: var(--gold); border-radius: 50%; }
  .art--burger { left: 30px; top: 290px; width: 150px; height: 140px; background: radial-gradient(circle, #c9c9c5, #56585c 72%); border-radius: 50%; }
  .art--pizza { left: 395px; top: 225px; width: 130px; height: 110px; background: radial-gradient(ellipse, #a9a9a5, #4b4d51 70%); border-radius: 50%; }

  .starters { position: absolute; left: 90px; top: 110px; width: 340px; height: 330px; background: radial-gradient(circle, var(--gold), var(--gold-deep)); border-radius: 50%; color: var(--ink); padding: 52px 42px 0 50px; }
  .starters__title { font-family: "Rye", serif; font-size: 38px; text-align: center; margin-bottom: 8px; }
  .dish { display: flex; justify-content: space-between; font-size: 10px; font-weight: 700; text-transform: uppercase; line-height: 1.55; }
  .dish small { display: block; font-size: 6.5px; font-weight: 500; line-height: 1; }

  .share { position: absolute; left: 40px; top: 600px; width: 460px; height: 110px; border: 1px solid var(--chalk-soft); display: flex; align-items: center; gap: 20px; padding: 0 20px; }
  .share__title { font-family: "Alfa Slab One", serif; font-size: 40px; color: var(--gold); }
  .share__list { display: grid; grid-template-columns: 1fr 1fr; gap: 6px 16px; font-size: 8px; font-weight: 700; text-transform: uppercase; color: var(--gold); }
  .share__list small { display: block; color: var(--chalk); font-size: 6.5px; font-weight: 500; }

  .kids-list { position: absolute; left: 200px; top: 110px; font-size: 9px; font-weight: 700; text-transform: uppercase; line-height: 1.6; list-style: none; }
  .kids-list li::before { content: "• "; color: var(--gold); }
  .kids-price { position: absolute; left: 440px; top: 60px; font-family: "Alfa Slab One", serif; color: var(--gold); font-size: 18px; }

  .burgers { position: absolute; left: 195px; top: 235px; width: 185px; display: grid; gap: 9px; }
  .burger__row { display: flex; justify-content: space-between; align-items: baseline; gap: 6px; }
  .burger__name { font-family: "Alfa Slab One", serif; color: var(--gold); font-size: 13px; line-height: 1; text-transform: uppercase; }
  .burger__price { font-size: 9px; color: var(--chalk); white-space: nowrap; }
  .burger__desc { font-size: 7px; color: var(--chalk-soft); margin-top: 2px; }

  .pizza-title { position: absolute; left: 390px; top: 355px; width: 135px; font-family: "Alfa Slab One", serif; color: var(--gold); font-size: 28px; line-height: 1; text-align: right; }
  .pizzas { position: absolute; left: 210px; top: 480px; list-style: none; }
  .pizza { font-family: "Marcellus SC", serif; color: var(--gold); font-size: 19px; line-height: 1; margin-bottom: 9px; }
  .pizza small { display: block; font-family: "Montserrat", sans-serif; color: var(--chalk); font-size: 6.5px; text-transform: uppercase; margin-top: 2px; }
</style>
</head>
<body>
<main class="spread">
  <section class="page page--left">
    <header class="brand" style="left:190px; top:40px; width:160px;">
      <div class="brand__mark"></div>
      <div class="brand__name">HEATHMERE</div>
      <div class="brand__sub">LODGE</div>
    </header>
    <div class="art art--rope" role="img" aria-label="Gold rope illustration"></div>
    <div class="starters">
      <h2 class="starters__title">STARTERS</h2>
      <div class="dish">• Garlic Bread<span>$6.50</span></div>
      <div class="dish">• Garlic Bread with Cheese<span>$7.00</span></div>
      <div class="dish"><span>• Potato Wedges<small>sour cream &amp; sweet chilli</small></span><span>$8.50</span></div>
      <div class="dish">• Beer Battered Onion Rings<span>$8.50</span></div>
      <div class="dish">• Salt and Pepper Squid<span>$12.00</span></div>
      <div class="dish"><span>• Hot Wings<small>with blue cheese dip</small></span><span>$11.50</span></div>
      <div class="dish"><span>• Bruschetta<small>tomato, basil &amp; balsamic</small></span><span>$9.50</span></div>
      <div class="dish"><span>• Oysters<small>natural or kilpatrick</small></span><span>MP</span></div>
    </div>
    <div class="art art--food" role="img" aria-label="Sketched illustration of starters and bread"></div>
    <div class="share">
      <h2 class="share__title">SHARE</h2>
      <div class="share__list">
        <div>• Trio of Dips $14<small>with toasted bread</small></div>
        <div>• Garlic Prawns $19<small>with crusty bread</small></div>
        <div>• Nachos $17.50<small>beans, cheese, sour cream</small></div>
        <div>• Bucket of Chips $9<small>with aioli</small></div>
        <div>• Crispy Chicken $16<small>sriracha mayo, tortilla</small></div>
      </div>
    </div>
  </section>

  <section class="page page--right">
    <header class="brand" style="left:30px; top:30px; width:150px;">
      <div class="brand__mark"></div>
      <div class="brand__name">HEATHMERE</div>
      <div class="brand__sub">LODGE</div>
    </header>
    <div class="art art--kids" role="img" aria-label="Hand-lettered Kids heading in a gold circle"></div>
    <ul class="kids-list">
      <li>Sausage, mash and corn cob</li>
      <li>Grilled chicken, mash and corn cob</li>
      <li>Penne bolognese</li>
      <li>Calamari with fries</li>
      <li>Dino nuggets with fries</li>
      <li>Fish and chips</li>
    </ul>
    <div class="kids-price">$12</div>
    <div class="art art--burger" role="img" aria-label="Sketched burger illustration"></div>
    <div class="burgers">
      <div><div class="burger__row"><span class="burger__name">Chicken Burger</span><span class="burger__price">$18.50</span></div><div class="burger__desc">Southern fried, slaw &amp; chipotle sauce</div></div>
      <div><div class="burger__row"><span class="burger__name">Beef Burger</span><span class="burger__price">$19.50</span></div><div class="burger__desc">Cheese, bacon, pickles &amp; relish</div></div>
      <div><div class="burger__row"><span class="burger__name">Vege Burger</span><span class="burger__price">$17.50</span></div><div class="burger__desc">Patty, salad &amp; aioli</div></div>
      <div><div class="burger__row"><span class="burger__name">Steak Sandwich</span><span class="burger__price">$21.00</span></div><div class="burger__desc">Onion, rocket &amp; relish</div></div>
      <div><div class="burger__row"><span class="burger__name">Fish Wrap</span><span class="burger__price">$18.00</span></div><div class="burger__desc">Slaw, lemon &amp; tartare</div></div>
    </div>
    <div class="art art--pizza" role="img" aria-label="Sketched pizza slice illustration"></div>
    <div class="pizza-title">9 INCH<br>PIZZA</div>
    <ul class="pizzas">
      <li class="pizza">Chicken Pesto<small>chicken, chorizo and pesto</small></li>
      <li class="pizza">Sicilian<small>pepperoni, olives, tomato, chilli &amp; oregano</small></li>
      <li class="pizza">Vegetarian<small>artichoke, olives, onion, capsicum</small></li>
      <li class="pizza">BBQ Meatlovers<small>selection of meats, BBQ sauce</small></li>
      <li class="pizza">Hawaiian<small>ham, pineapple</small></li>
    </ul>
  </section>
</main>
</body>
</html>
```